Smile club flyer design

I am launching an office smile club and would like a design that sits my branding and that is appealing to customers. I have a design (I need a new one) that has all the information.
My website is maplecrestdentalcarewv.com
Brand color is green. The design can be any color

Target Market(s)

Ages 30+

Industry/Entity Type

Dental

Font styles to use
Serif

Requirements
Must have
• Appealing to patients

```html
<!DOCTYPE html>
<html lang="en">
<head>
<meta charset="utf-8">
<title>Maplecrest Dental Care – Smile Club Membership</title>
<link href="https://fonts.googleapis.com/css2?family=Montserrat:wght@400;500;600;700;800;900&display=swap" rel="stylesheet">
<style>
  :root {
    --navy: #13182b;
    --teal: #10b8a6;
    --teal-dark: #0f9a8c;
    --green: #0c9242;
    --green-deep: #0b6a37;
    --lime: #8cc63f;
    --cream: #e6f3c9;
    --white: #ffffff;
    --ink: #1c1f2a;
    --page: #e9e9e9;
  }
  * { box-sizing: border-box; margin: 0; padding: 0; }
  html, body { width: 1200px; height: 1200px; overflow: hidden; }
  body {
    background: var(--page);
    font-family: "Montserrat", sans-serif;
    color: var(--ink);
  }
  .flyer {
    position: absolute;
    left: 220px; top: 30px;
    width: 760px; height: 1140px;
    background: var(--navy);
    overflow: hidden;
  }
  .flyer-bg { position: absolute; inset: 0; }
  .abs { position: absolute; }
  .center { left: 0; width: 760px; text-align: center; }

  /* Brand */
  .brand-name {
    top: 38px; font-size: 50px; font-weight: 700; color: var(--green);
    letter-spacing: -0.5px; line-height: 1;
  }
  .brand-sub {
    top: 94px; font-size: 20px; font-weight: 700; color: var(--green);
    letter-spacing: 6px; line-height: 1;
  }
  .brand-sub::before, .brand-sub::after {
    content: ""; display: inline-block; width: 26px; height: 2px;
    background: var(--green); vertical-align: middle; margin: 0 8px;
  }

  /* Headline */
  .intro { top: 160px; font-size: 26px; font-weight: 400; letter-spacing: 3px; color: var(--green-deep); }
  .club-title { top: 192px; font-size: 64px; font-weight: 900; color: var(--green-deep); letter-spacing: -1px; line-height: 1; }
  .club-sub { top: 258px; font-size: 32px; font-weight: 800; color: var(--green-deep); letter-spacing: 3px; line-height: 1; }

  .art { border-radius: 24px; }
  .art-tools-left { left: 0; top: 190px; width: 185px; height: 230px; background: linear-gradient(160deg, rgba(200,210,215,.35), rgba(150,160,170,.15)); }
  .art-drill { left: 585px; top: 118px; width: 140px; height: 160px; background: linear-gradient(160deg, rgba(190,200,205,.45), rgba(130,140,150,.2)); }
  .art-tooth { left: 575px; top: 320px; width: 150px; height: 125px; background: linear-gradient(180deg, rgba(255,255,255,.55), rgba(170,175,230,.35)); }

  /* Plans */
  .plan {
    position: absolute; width: 225px; background: var(--white);
    border-radius: 20px; overflow: hidden;
  }
  .plan-head {
    background: var(--green); color: var(--white); text-align: center;
    height: 68px; padding-top: 16px; position: relative;
  }
  .plan-name { font-size: 24px; font-weight: 800; color: var(--cream); line-height: 1; letter-spacing: -0.3px; }
  .plan-type { font-size: 16px; font-weight: 500; line-height: 1; margin-top: 7px; }
  .plan-price {
    position: relative; background: var(--teal); height: 58px; text-align: center;
    color: var(--white); border-radius: 0 0 50% 50% / 0 0 12px 12px; padding-top: 14px;
  }
  .plan-price::before {
    content: ""; position: absolute; left: 0; top: 0; width: 100%; height: 10px;
    background: var(--lime); border-radius: 0 0 50% 50% / 0 0 10px 10px;
  }
  .plan-price::after {
    content: ""; position: absolute; left: 0; top: -4px; width: 100%; height: 8px;
    background: var(--green); border-radius: 0 0 50% 50% / 0 0 8px 8px;
  }
  .amount { font-size: 35px; font-weight: 800; line-height: 1; }
  .per { font-size: 21px; font-weight: 400; }
  .features { list-style: none; padding: 14px 10px 0 14px; }
  .features li {
    position: relative; padding-left: 19px; font-size: 13.5px; line-height: 18px;
    font-weight: 500; margin-bottom: 17px;
  }
  .features li svg { position: absolute; left: 0; top: 3px; width: 13px; height: 13px; }

  .plan-core { left: 32px; top: 499px; height: 325px; }
  .plan-bright { left: 266px; top: 499px; height: 325px; }
  .plan-total { left: 499px; top: 499px; height: 325px; }
  .plan-refresh { left: 32px; top: 837px; height: 265px; }
  .plan-refresh .plan-head { padding-top: 18px; }
  .plan-refresh .amount { font-size: 36px; }
  .new-tag {
    position: absolute; left: 0; top: 0; width: 66px; height: 42px;
    background: var(--teal); border-radius: 0 0 30px 0;
    font-size: 14px; font-weight: 800; color: var(--white); padding: 12px 0 0 12px;
    text-align: left;
  }

  /* Financing */
  .finance-label { left: 290px; width: 410px; top: 853px; text-align: center; color: var(--white); font-size: 12px; font-weight: 500; letter-spacing: .5px; }
  .lender {
    position: absolute; top: 876px; width: 202px; height: 49px;
    background: var(--white); border-radius: 8px; border: 2px solid var(--teal);
    display: flex; align-items: center; justify-content: center; gap: 8px;
    font-size: 26px; font-weight: 700; color: var(--ink);
  }
  .lender-dot { width: 16px; height: 16px; border-radius: 50%; background: var(--teal-dark); }
  .lender-a { left: 292px; }
  .lender-b { left: 509px; }
  .plans-note { left: 290px; width: 410px; top: 937px; text-align: center; color: var(--white); font-size: 12.5px; font-weight: 500; letter-spacing: .5px; }
  .fee-pill {
    left: 348px; top: 975px; width: 308px; height: 27px; border-radius: 14px;
    background: var(--teal-dark); color: var(--white); font-size: 11px; font-weight: 500;
    text-align: center; line-height: 27px;
  }
  .join { left: 290px; width: 410px; top: 1030px; text-align: center; color: var(--teal); font-size: 22px; font-weight: 500; letter-spacing: .5px; }
  .phone { left: 270px; width: 450px; top: 1060px; text-align: center; color: var(--white); font-size: 45px; font-weight: 800; letter-spacing: 1px; }
</style>
</head>
<body>
<main class="flyer">
  <svg class="flyer-bg" width="760" height="1140" viewBox="0 0 760 1140">
    <defs>
      <path id="arc-top" d="M160 340 A400 400 0 0 0 600 340"/>
      <path id="arc-bottom" d="M150 370 A420 420 0 0 0 610 370"/>
      <linearGradient id="ring-grad" x1="0" y1="0" x2="0" y2="1">
        <stop offset="0" stop-color="#9fd9d5"/>
        <stop offset="1" stop-color="#4f6bc6"/>
      </linearGradient>
    </defs>
    <rect width="760" height="1140" fill="var(--navy)"/>
    <path d="M0 143 H760 V190 A390 364 0 0 1 0 190 Z" fill="var(--teal)"/>
    <rect width="760" height="143" fill="var(--white)"/>
    <path d="M125 143 A255 202 0 0 0 635 143 Z" fill="var(--white)"/>
    <circle cx="808" cy="1120" r="66" fill="none" stroke="url(#ring-grad)" stroke-width="18"/>
    <text font-family="Montserrat, sans-serif" font-size="21" font-weight="500" fill="#ffffff" letter-spacing="1.5">
      <textPath href="#arc-top" startOffset="50%" text-anchor="middle">AFFORDABLE DENTAL CARE</textPath>
    </text>
    <text font-family="Montserrat, sans-serif" font-size="21" font-weight="800" fill="#ffffff" letter-spacing="1">
      <textPath href="#arc-bottom" startOffset="50%" text-anchor="middle">NO INSURANCE REQUIRED</textPath>
    </text>
  </svg>

  <div class="abs center brand-name">Maplecrest</div>
  <div class="abs center brand-sub">DENTAL CARE</div>

  <div class="abs art art-tools-left" role="img" aria-label="Dental mirror and explorer instruments"></div>
  <div class="abs art art-drill" role="img" aria-label="Dental handpiece drill"></div>
  <div class="abs art art-tooth" role="img" aria-label="Shiny white tooth with circular arrows"></div>

  <div class="abs center intro">INTRODUCING</div>
  <h1 class="abs center club-title">SMILE CLUB</h1>
  <div class="abs center club-sub">MEMBERSHIP</div>

  <section class="plan plan-core">
    <div class="plan-head"><div class="plan-name">CORE CARE</div><div class="plan-type">Preventive</div></div>
    <div class="plan-price"><span class="amount">$39</span><span class="per">/month</span></div>
    <ul class="features">
      <li><svg viewBox="0 0 14 14"><circle cx="7" cy="7" r="6" fill="none" stroke="#17b26a" stroke-width="1.6"/><path d="M4 7.2l2.2 2.2L12.5 3" fill="none" stroke="#17b26a" stroke-width="1.8"/></svg>Comprehensive Annual Exam</li>
      <li><svg viewBox="0 0 14 14"><circle cx="7" cy="7" r="6" fill="none" stroke="#17b26a" stroke-width="1.6"/><path d="M4 7.2l2.2 2.2L12.5 3" fill="none" stroke="#17b26a" stroke-width="1.8"/></svg>2 Professional Cleanings per Year</li>
      <li><svg viewBox="0 0 14 14"><circle cx="7" cy="7" r="6" fill="none" stroke="#17b26a" stroke-width="1.6"/><path d="M4 7.2l2.2 2.2L12.5 3" fill="none" stroke="#17b26a" stroke-width="1.8"/></svg>Routine Bitewing X-rays</li>
      <li><svg viewBox="0 0 14 14"><circle cx="7" cy="7" r="6" fill="none" stroke="#17b26a" stroke-width="1.6"/><path d="M4 7.2l2.2 2.2L12.5 3" fill="none" stroke="#17b26a" stroke-width="1.8"/></svg>10% Saving on Treatment</li>
    </ul>
  </section>

  <section class="plan plan-bright">
    <div class="plan-head"><div class="plan-name">BRIGHT</div><div class="plan-type">Cosmetic</div></div>
    <div class="plan-price"><span class="amount">$59</span><span class="per">/month</span></div>
    <ul class="features">
      <li><svg viewBox="0 0 14 14"><circle cx="7" cy="7" r="6" fill="none" stroke="#17b26a" stroke-width="1.6"/><path d="M4 7.2l2.2 2.2L12.5 3" fill="none" stroke="#17b26a" stroke-width="1.8"/></svg>Annual In-Office Whitening<br>(Top &amp; Bottom)</li>
      <li><svg viewBox="0 0 14 14"><circle cx="7" cy="7" r="6" fill="none" stroke="#17b26a" stroke-width="1.6"/><path d="M4 7.2l2.2 2.2L12.5 3" fill="none" stroke="#17b26a" stroke-width="1.8"/></svg>Custom Whitening Trays</li>
      <li><svg viewBox="0 0 14 14"><circle cx="7" cy="7" r="6" fill="none" stroke="#17b26a" stroke-width="1.6"/><path d="M4 7.2l2.2 2.2L12.5 3" fill="none" stroke="#17b26a" stroke-width="1.8"/></svg>15% Savings on Elective Treatment</li>
    </ul>
  </section>

  <section class="plan plan-total">
    <div class="plan-head"><div class="plan-name">TOTAL SMILE</div><div class="plan-type">Periodontal</div></div>
    <div class="plan-price"><span class="amount">$89</span><span class="per">/month</span></div>
    <ul class="features">
      <li><svg viewBox="0 0 14 14"><circle cx="7" cy="7" r="6" fill="none" stroke="#17b26a" stroke-width="1.6"/><path d="M4 7.2l2.2 2.2L12.5 3" fill="none" stroke="#17b26a" stroke-width="1.8"/></svg>3-4 Perio Maintenance Visits per Year</li>
      <li><svg viewBox="0 0 14 14"><circle cx="7" cy="7" r="6" fill="none" stroke="#17b26a" stroke-width="1.6"/><path d="M4 7.2l2.2 2.2L12.5 3" fill="none" stroke="#17b26a" stroke-width="1.8"/></svg>1 Comprehensive Exam</li>
      <li><svg viewBox="0 0 14 14"><circle cx="7" cy="7" r="6" fill="none" stroke="#17b26a" stroke-width="1.6"/><path d="M4 7.2l2.2 2.2L12.5 3" fill="none" stroke="#17b26a" stroke-width="1.8"/></svg>Diagnostic X-rays</li>
      <li><svg viewBox="0 0 14 14"><circle cx="7" cy="7" r="6" fill="none" stroke="#17b26a" stroke-width="1.6"/><path d="M4 7.2l2.2 2.2L12.5 3" fill="none" stroke="#17b26a" stroke-width="1.8"/></svg>15% Savings on Restorative &amp; Elective Care</li>
    </ul>
  </section>

  <section class="plan plan-refresh">
    <div class="plan-head">
      <div class="new-tag">NEW</div>
      <div class="plan-name">SMILE</div><div class="plan-type">Refresh Package</div>
    </div>
    <div class="plan-price"><span class="amount">$499</span></div>
    <ul class="features">
      <li><svg viewBox="0 0 14 14"><circle cx="7" cy="7" r="6" fill="none" stroke="#17b26a" stroke-width="1.6"/><path d="M4 7.2l2.2 2.2L12.5 3" fill="none" stroke="#17b26a" stroke-width="1.8"/></svg>Cleaning +<br>Comprehensive Exam +<br>Whitening</li>
      <li><svg viewBox="0 0 14 14"><circle cx="7" cy="7" r="6" fill="none" stroke="#17b26a" stroke-width="1.6"/><path d="M4 7.2l2.2 2.2L12.5 3" fill="none" stroke="#17b26a" stroke-width="1.8"/></svg>Limited Time Offer</li>
    </ul>
  </section>

  <div class="abs finance-label">FLEXIBLE FINANCING FOR TREATMENT:</div>
  <div class="lender lender-a"><span class="lender-dot"></span>FlexiPay</div>
  <div class="lender lender-b"><span class="lender-dot"></span>Plumly</div>
  <div class="abs plans-note">PAYMENT PLANS AVAILABLE</div>
  <div class="abs fee-pill">*$49 Lifetime Activation Fee (Non-Refundable)</div>
  <div class="abs join">JOIN SMILE CLUB TODAY!</div>
  <div class="abs phone">0865-555-014</div>
</main>
</body>
</html>
```